Need 2 sided card for Loomfield Goods Co. Logo supplied.

I am looking for a business card for my online craft supply business.

I have a very simple design already which I am kind of happy with (see attached pdf) - but would like suggestions for something a little more creative. Design MUST be clean. Super clean! Think thin lines and not blocks of color...

Design must be clean and crisp. No other colors other than in palette (see link below)

I would also like to possible incorporate my tagline - maybe on the front but definitely on the back:
"HollowReed Ideas & Hobby Materials"

Logo file is supplied, but I think spacing on the card may required the wording to be moved underneaths the camera icon - which is fine. Font in logo is Maven Pro. OPEN TO USE OF OTHER FONTS ON CARD BUT MUST BE CLEAN DESIGN.

FRONT OF CARD
All information on attached pdf is correct and should be shown in your design.

BACK OF CARD
Needs to show www.tindalerow.example and maybe logo repeat and tagline.

SIZE
New Zealand sized - meaning finished card will be 90 x 55mm
Printing requirements: printed area is 90mm x 55mm with a 2mm bleed all round.

COLORS
Color palette used in logo can be seen here for HEX and RGB reference: http://www.huebankly.example/palette/8627410/website

NOTE: PAYMENT WILL BE MADE FOR THE BEST DESIGN - EVEN IF I DECIDE NOT TO USE IT.
Updates

Thank you all so much for your designs. I will be providing feedback to ALL designers tomorrow. This weekend is a holiday weekend here in New Zealand and so no work for a few days. Thank-you again - I appreciate your time and creativity!

Industry/Entity Type

Camera

Font styles to use
Other font styles liked:
• Maven Pro - open to others

Requirements
Must have
• Clean design. Logo must be prominent for brand recognition. All contact information must be shown.
Nice to have
• Tagline - at least on reverse

```html
<!DOCTYPE html>
<html lang="en">
<head>
<meta charset="utf-8">
<title>Loomfield Goods Co. — Business Card, Front and Back</title>
<link rel="stylesheet" href="https://fonts.googleapis.com/css2?family=Maven+Pro:wght@400;500&display=swap">
<style>
  :root {
    --board: #595959;
    --card: #ffffff;
    --red: #f4411e;
    --lime: #c9d321;
    --cream: #f1f0c6;
    --ink: #4f5454;
    --text: #333838;
    --green: #5cc57c;
    --label: #ffffff;
  }
  * { margin: 0; padding: 0; box-sizing: border-box; }
  html, body { width: 1200px; height: 758px; overflow: hidden; }
  body {
    background: var(--board);
    font-family: "Maven Pro", sans-serif;
    position: relative;
  }
  .side-label {
    position: absolute;
    color: var(--label);
    font-size: 34px;
    font-weight: 400;
    letter-spacing: 1px;
    line-height: 1;
  }
  .side-label--front { left: 604px; top: 24px; }
  .side-label--back { right: 614px; top: 394px; }

  .card {
    position: absolute;
    width: 568px;
    height: 347px;
    background: var(--card);
    overflow: hidden;
  }
  .card--front { left: 22px; top: 22px; }
  .card--back { left: 600px; top: 392px; }

  .stripe { position: absolute; top: 0; bottom: 0; width: 16px; }
  .stripe--lime { background: var(--lime); }
  .stripe--red { background: var(--red); }

  .rule-cream { position: absolute; right: 0; height: 9px; background: var(--cream); }
  .tagline-band {
    position: absolute;
    right: 0;
    background: var(--red);
    color: #fff;
    display: flex;
    align-items: center;
    justify-content: center;
    white-space: nowrap;
  }

  /* Front */
  .card--front .stripe--lime { left: 18px; }
  .card--front .stripe--red { left: 41px; }
  .card--front .rule-cream { left: 56px; top: 222px; }
  .card--front .tagline-band { left: 56px; top: 236px; height: 34px; font-size: 23px; }
  .front-brand {
    position: absolute;
    left: 56px; right: 0; top: 40px;
    display: flex; flex-direction: column; align-items: center;
  }
  .brand-dot { border-radius: 50%; background: var(--red); }
  .front-brand .brand-dot { width: 70px; height: 70px; margin-bottom: 22px; }
  .front-brand .brand-name {
    color: var(--ink);
    font-size: 44px;
    font-weight: 400;
    line-height: 1;
  }
  .front-url {
    position: absolute;
    left: 56px; right: 0; top: 293px;
    text-align: center;
    color: var(--text);
    font-size: 18px;
    letter-spacing: 0.5px;
  }

  /* Back */
  .card--back .stripe--lime { left: 159px; }
  .card--back .stripe--red { left: 181px; }
  .card--back .rule-cream { left: 197px; top: 256px; height: 10px; }
  .card--back .tagline-band { left: 197px; top: 274px; height: 30px; font-size: 17px; }
  .back-brand {
    position: absolute;
    left: 0; width: 159px; top: 110px;
    display: flex; flex-direction: column; align-items: center;
  }
  .back-brand .brand-dot { width: 34px; height: 34px; margin-bottom: 12px; }
  .back-brand .brand-name {
    color: var(--ink);
    font-size: 20px;
    font-weight: 400;
    line-height: 1.15;
    text-align: center;
  }
  .contact-list {
    position: absolute;
    left: 212px; top: 47px;
    list-style: none;
  }
  .contact-item {
    display: flex; align-items: center;
    height: 33px;
    color: var(--text);
    font-size: 18px;
    white-space: nowrap;
  }
  .contact-icon { width: 24px; height: 24px; margin-right: 12px; flex: none; }
</style>
</head>
<body>

  <div class="side-label side-label--front">&lt; Front Side</div>
  <div class="side-label side-label--back">Back Side&gt;</div>

  <section class="card card--front" aria-label="Card front">
    <div class="stripe stripe--lime"></div>
    <div class="stripe stripe--red"></div>
    <div class="front-brand">
      <span class="brand-dot"></span>
      <span class="brand-name">Loomfield Goods Co.</span>
    </div>
    <div class="rule-cream"></div>
    <div class="tagline-band">HollowReed Ideas &amp; Hobby Materials</div>
    <div class="front-url">www.tindalerow.example</div>
  </section>

  <section class="card card--back" aria-label="Card back">
    <div class="back-brand">
      <span class="brand-dot"></span>
      <span class="brand-name">Loomfield<br>Goods Co.</span>
    </div>
    <div class="stripe stripe--lime"></div>
    <div class="stripe stripe--red"></div>

    <ul class="contact-list">
      <li class="contact-item">
        <svg class="contact-icon" viewBox="0 0 24 24" aria-hidden="true">
          <circle cx="12" cy="12" r="11.5" fill="#fbd3c9"/>
          <circle cx="12" cy="12" r="9.5" fill="var(--red)"/>
          <path d="M8.6 7.2c.5-.4 1-.3 1.3.2l1 1.6c.3.5.2.9-.2 1.2l-.6.5c.5 1.2 1.4 2.2 2.6 2.8l.5-.6c.3-.4.8-.5 1.2-.2l1.6 1c.5.3.6.8.2 1.3l-.7.8c-.6.6-1.6.7-2.7.1-2.1-1.1-3.8-2.9-4.8-5-.5-1.1-.4-2 .2-2.6z" fill="#fff"/>
        </svg>
        +64 (0) 3 555 0142
      </li>
      <li class="contact-item">
        <svg class="contact-icon" viewBox="0 0 24 24" aria-hidden="true">
          <circle cx="12" cy="12" r="11.5" fill="#eef2b6"/>
          <circle cx="12" cy="12" r="9.5" fill="var(--lime)"/>
          <rect x="9" y="6.5" width="6" height="11" rx="1" fill="none" stroke="#fff" stroke-width="1.4"/>
          <circle cx="12" cy="15.5" r="0.8" fill="#fff"/>
        </svg>
        +64 (0) 21 555 01873
      </li>
      <li class="contact-item">
        <svg class="contact-icon" viewBox="0 0 24 24" aria-hidden="true">
          <circle cx="12" cy="12" r="11.5" fill="#cdeed7"/>
          <circle cx="12" cy="12" r="9.5" fill="var(--green)"/>
          <rect x="7" y="8.5" width="10" height="7" rx="1" fill="none" stroke="#fff" stroke-width="1.3"/>
          <path d="M7.3 9l4.7 3.6L16.7 9" fill="none" stroke="#fff" stroke-width="1.3"/>
        </svg>
        nell.harrow@loomfieldgoods.example
      </li>
      <li class="contact-item">
        <svg class="contact-icon" viewBox="0 0 24 24" aria-hidden="true">
          <circle cx="12" cy="12" r="11.5" fill="#d4d6d6"/>
          <circle cx="12" cy="12" r="9.5" fill="var(--ink)"/>
        </svg>
        social.example/loomfieldgoods
      </li>
      <li class="contact-item">
        <svg class="contact-icon" viewBox="0 0 24 24" aria-hidden="true">
          <circle cx="12" cy="12" r="11.5" fill="#cdeed7"/>
          <circle cx="12" cy="12" r="9.5" fill="var(--green)"/>
          <rect x="8" y="10" width="8" height="7" rx="0.8" fill="none" stroke="#fff" stroke-width="1.3"/>
          <path d="M10 10V8.8a2 2 0 0 1 4 0V10" fill="none" stroke="#fff" stroke-width="1.3"/>
        </svg>
        www.tindalerow.example
      </li>
      <li class="contact-item">
        <svg class="contact-icon" viewBox="0 0 24 24" aria-hidden="true">
          <circle cx="12" cy="12" r="11.5" fill="#fbd3c9"/>
          <circle cx="12" cy="12" r="9.5" fill="var(--red)"/>
          <circle cx="12" cy="12" r="5.2" fill="none" stroke="#fff" stroke-width="1.2"/>
          <ellipse cx="12" cy="12" rx="2.3" ry="5.2" fill="none" stroke="#fff" stroke-width="1.1"/>
          <path d="M6.8 12h10.4M7.6 9.4h8.8M7.6 14.6h8.8" stroke="#fff" stroke-width="1"/>
        </svg>
        www.loomfieldgoods.example
      </li>
    </ul>

    <div class="rule-cream"></div>
    <div class="tagline-band">HollowReed Ideas &amp; Hobby Materials</div>
  </section>

</body>
</html>
```